PostLoopy Social Sharing Platform Needs a Redesign (2 pages / Design only)

PostLoopy is a popular social sharing platform for bloggers and marketers. The site has been quite popular for a few years now, but the site's design is looking quite dated. We're looking for a brand new design to give the service a facelift.

We are looking for a modern and fresh design that keeps all the existing functionality intact. Would prefer designs that incorporate the color blue in them.

We would like the two attached screenshots to be redesigned and submitted - using he same content. Please do not submit a redesign of the front page (non-logged in version). Redesign the 2 attached pages only, and the final deliverable is these two pages as layered PSD files.

Target Market(s)

bloggers, internet marketers

Industry/Entity Type

Social

Number of Pages Required

2 page

Requirements
Must have
• All existing functionality must be intact as seen from the screenshots.
Should not have
• Please do not submit designs based on existing front page (non-logged in version). Use attached screenshots (file 1 and 2) as a guide of existing functionality.

```html
<!DOCTYPE html>
<html lang="en">
<head>
<meta charset="utf-8">
<title>PostLoopy Dashboard</title>
<link href="https://fonts.googleapis.com/css2?family=Roboto:wght@300;400;500;700&display=swap" rel="stylesheet">
<style>
:root{
  --blue:#1b82d6;
  --blue-dark:#0d66b8;
  --blue-deep:#0a5aa3;
  --blue-light:#d3e8f9;
  --blue-line:#8fc0ea;
  --ink:#2d2d2d;
  --muted:#6b6b6b;
  --line:#dcdcdc;
  --orange:#f39a1e;
  --red:#e0463c;
  --green:#43a047;
  --charcoal:#2f2f2f;
  --footer-dark:#0b5fae;
}
*{box-sizing:border-box;margin:0;padding:0}
html,body{width:1200px;height:2415px;overflow:hidden}
body{font-family:'Roboto',Arial,sans-serif;color:var(--ink);background:#fff;position:relative}
a{color:inherit;text-decoration:none}
.topbar{height:41px;background:var(--blue);color:#e6f1fb;font-size:14px;display:flex;align-items:center;justify-content:space-between;padding:0 67px}
.topbar .welcome{display:flex;align-items:center;gap:10px}
.topbar .mini-avatar{width:22px;height:22px;border-radius:3px;background:linear-gradient(#c8a58a,#6d5a4e)}
.topbar .tools{display:flex;gap:34px;align-items:center}
.topbar .tools span{display:flex;align-items:center;gap:8px}
.header{height:108px;display:flex;align-items:center;justify-content:space-between;padding:0 67px;border-bottom:1px solid #eee}
.logo{font-size:34px;font-weight:700;color:var(--blue-deep);letter-spacing:-0.5px}
.nav{display:flex;gap:32px;font-size:15px;color:#444;align-items:center}
.nav .active{color:var(--blue)}
.banner{height:143px;background:linear-gradient(100deg,#1a87dc,#0f6fc6 60%,#1583d6);display:flex;align-items:center;padding:0 67px}
.banner h1{font-weight:300;color:#fff;font-size:58px}
.main{position:absolute;left:67px;top:335px;width:704px}
.side{position:absolute;left:791px;top:340px;width:342px}
.section-head{display:flex;align-items:baseline;gap:14px}
.section-head h2{font-weight:400;font-size:25px;color:var(--blue)}
.section-head .sub{font-size:14px;color:#555;border-left:1px solid #ccc;padding-left:14px}
.members{display:grid;grid-template-columns:repeat(4,176px);row-gap:17px;margin-top:28px}
.member{display:flex;gap:12px;align-items:center}
.avatar{width:50px;height:50px;border-radius:50%;flex:none}
.member .name{font-size:12px;color:#333;margin-bottom:6px}
.follow{display:inline-flex;align-items:center;gap:5px;font-size:12px;color:#333;border:1px solid var(--line);border-radius:3px;padding:4px 9px;background:#fff}
.follow svg{width:11px;height:11px}
.feed-head{margin-top:66px;display:flex;align-items:center;gap:26px}
.feed-head h2{font-weight:400;font-size:25px;color:var(--blue)}
.feed-head .opt{font-size:14px;color:#555}
.tweet{position:relative;height:132px;border:1px solid var(--blue-line);margin-top:10px;padding:13px 14px 0 80px;background:#fff}
.feed-head + .tweet{margin-top:26px}
.tweet.hl{background:var(--blue-light)}
.tweet .avatar{position:absolute;left:14px;top:11px}
.tweet .meta{font-size:14px}
.tweet .handle{color:var(--blue)}
.dot{display:inline-block;width:9px;height:9px;border-radius:50%;background:var(--orange);margin:0 4px}
.tweet .cat{color:#555}
.tweet p{font-size:12.5px;line-height:16px;color:#444;margin-top:2px}
.tweet .link{color:var(--blue)}
.actions{position:absolute;left:80px;bottom:10px;display:flex;gap:18px;align-items:center;font-size:12px;color:#333}
.actions span{display:flex;align-items:center;gap:5px}
.pill{display:inline-flex;align-items:center;gap:4px;font-size:10px}
.pill b{display:inline-block;height:16px;padding:0 7px;line-height:16px;border-radius:2px;color:#fff;font-weight:500}
.pill .like{background:#4a68a8}
.pill .plus{background:#fff;color:var(--red);border:1px solid var(--line)}
.pill i{font-style:normal;border:1px solid var(--line);padding:0 4px;height:16px;line-height:14px;color:#555;background:#fff}
.spinner{display:block;margin:48px auto 0}
.credits{height:203px;background:var(--blue-deep);color:#fff;text-align:center;padding-top:22px}
.credits .label{font-size:25px;font-weight:300}
.credits .num{font-size:62px;font-weight:300;line-height:62px;letter-spacing:1px}
.credits .btn{display:flex;align-items:center;justify-content:center;gap:12px;width:254px;height:55px;margin:16px auto 0;background:#3a9ee8;font-size:22px;font-weight:300}
.engage{margin-top:60px}
.engage .list{display:grid;grid-template-columns:180px 160px;row-gap:16px;margin-top:28px}
.slide{margin-top:30px;height:121px;background:linear-gradient(180deg,#1c1c1c,#0d0d0d);position:relative}
.arrow{position:absolute;top:50%;width:26px;height:38px;margin-top:-19px;background:rgba(255,255,255,.75);display:flex;align-items:center;justify-content:center}
.arrow.l{left:0}.arrow.r{right:0}
.card-title{text-align:center;font-size:18px;color:#333;margin-top:20px;line-height:25px}
.card-text{text-align:center;font-size:13px;color:#555;line-height:19px;margin-top:10px;padding:0 10px}
.dots{display:flex;justify-content:center;gap:14px;margin-top:12px}
.dots i{width:6px;height:6px;border-radius:50%;background:#ccc}
.dots i:first-child{background:#888}
.blog-img{margin-top:30px;height:230px;background:radial-gradient(circle at 50% 55%,#6fa8dc,#2f6db5 70%);position:relative}
.contest{position:absolute;top:2031px;left:0;width:1200px;height:134px;background:var(--charcoal);display:flex;align-items:center;justify-content:center;gap:28px;color:#fff;font-size:23px;font-weight:300}
.contest .btn{background:#fff;color:var(--ink);font-size:13px;font-weight:400;padding:10px 22px;border-radius:2px}
.footer{position:absolute;top:2165px;left:0;width:1200px;height:176px;background:var(--blue);display:flex;align-items:center;justify-content:space-between;padding:0 67px;color:#fff}
.footer .logo{color:#fff}
.footer nav{display:flex;gap:28px;font-size:16px}
.bottom{position:absolute;top:2341px;left:0;width:1200px;height:74px;background:var(--footer-dark);display:flex;align-items:center;justify-content:space-between;padding:0 67px;color:#cfe3f6;font-size:11px}
.social{display:flex;gap:30px}
.social i{width:16px;height:16px;border-radius:50%;background:#7fb2e3}
.totop{position:absolute;left:580px;width:40px;height:40px;border:1px solid #6ea3d8;display:flex;align-items:center;justify-content:center}
</style>
</head>
<body>

<header class="topbar">
  <div class="welcome">Welcome, Mark Delvin <span class="mini-avatar" role="img" aria-label="User profile photo"></span></div>
  <div class="tools">
    <span><svg width="12" height="12" viewBox="0 0 12 12"><circle cx="6" cy="3.5" r="2.5" fill="#e6f1fb"/><path d="M1 12c0-3 2.5-5 5-5s5 2 5 5z" fill="#e6f1fb"/></svg>Logout</span>
    <span><svg width="14" height="10" viewBox="0 0 14 10"><rect x=".5" y=".5" width="13" height="9" fill="none" stroke="#e6f1fb"/><path d="M.5 .5l6.5 5 6.5-5" fill="none" stroke="#e6f1fb"/></svg>info@postloopy.com</span>
    <span><svg width="12" height="12" viewBox="0 0 12 12"><circle cx="2.5" cy="6" r="2" fill="#e6f1fb"/><circle cx="9.5" cy="2.5" r="2" fill="#e6f1fb"/><circle cx="9.5" cy="9.5" r="2" fill="#e6f1fb"/><path d="M2.5 6l7-3.5M2.5 6l7 3.5" stroke="#e6f1fb"/></svg>follow us ▾</span>
    <span><svg width="13" height="13" viewBox="0 0 13 13"><circle cx="6.5" cy="6.5" r="6" fill="#e6f1fb"/></svg>▾</span>
  </div>
</header>

<div class="header">
  <div class="logo">PostLoopy</div>
  <nav class="nav">
    <a class="active">Dashboard</a><a>Chirper Followers</a><a>Submit Tweet</a><a>Activity Summary</a><a>Buy Credits</a><a>Affiliates</a>
    <svg width="16" height="16" viewBox="0 0 16 16"><circle cx="8" cy="8" r="5" fill="none" stroke="#555" stroke-width="3" stroke-dasharray="3 2"/><circle cx="8" cy="8" r="2" fill="#555"/></svg>
    <svg width="15" height="15" viewBox="0 0 15 15"><circle cx="6" cy="6" r="4.5" fill="none" stroke="#555" stroke-width="2"/><path d="M9.5 9.5l4 4" stroke="#555" stroke-width="2"/></svg>
  </nav>
</div>

<section class="banner"><h1>Dashboard</h1></section>

<main class="main">
  <div class="section-head"><h2>Featured Members</h2><span class="sub">See all members</span></div>
  <div class="members">
    <div class="member"><span class="avatar" style="background:#b07a62" role="img" aria-label="Member photo"></span><div><div class="name">Annaclickcafe</div><span class="follow"><svg viewBox="0 0 11 11"><circle cx="4" cy="3" r="2.3" fill="#4a90d9"/><path d="M0 11c0-3 2-4.5 4-4.5s4 1.5 4 4.5z" fill="#4a90d9"/></svg>Follow</span></div></div>
    <div class="member"><span class="avatar" style="background:#d9b98a" role="img" aria-label="Member photo"></span><div><div class="name">timefreelancer</div><span class="follow"><svg viewBox="0 0 11 11"><circle cx="4" cy="3" r="2.3" fill="#4a90d9"/><path d="M0 11c0-3 2-4.5 4-4.5s4 1.5 4 4.5z" fill="#4a90d9"/></svg>Follow</span></div></div>
    <div class="member"><span class="avatar" style="background:#8d6656" role="img" aria-label="Member photo"></span><div><div class="name">NoraDeane</div><span class="follow"><svg viewBox="0 0 11 11"><circle cx="4" cy="3" r="2.3" fill="#4a90d9"/><path d="M0 11c0-3 2-4.5 4-4.5s4 1.5 4 4.5z" fill="#4a90d9"/></svg>Follow</span></div></div>
    <div class="member"><span class="avatar" style="background:radial-gradient(#f2c14e,#e86a5a 50%,#5aa0e0)" role="img" aria-label="Member brand image"></span><div><div class="name">crossnetideas</div><span class="follow"><svg viewBox="0 0 11 11"><circle cx="4" cy="3" r="2.3" fill="#4a90d9"/><path d="M0 11c0-3 2-4.5 4-4.5s4 1.5 4 4.5z" fill="#4a90d9"/></svg>Follow</span></div></div>
    <div class="member"><span class="avatar" style="background:#2a2a2a;border-radius:10px" role="img" aria-label="Member brand image"></span><div><div class="name">GrowPlot</div><span class="follow"><svg viewBox="0 0 11 11"><circle cx="4" cy="3" r="2.3" fill="#4a90d9"/><path d="M0 11c0-3 2-4.5 4-4.5s4 1.5 4 4.5z" fill="#4a90d9"/></svg>Follow</span></div></div>
    <div class="member"><span class="avatar" style="background:#c99a84" role="img" aria-label="Member photo"></span><div><div class="name">Ilena</div><span class="follow"><svg viewBox="0 0 11 11"><circle cx="4" cy="3" r="2.3" fill="#4a90d9"/><path d="M0 11c0-3 2-4.5 4-4.5s4 1.5 4 4.5z" fill="#4a90d9"/></svg>Follow</span></div></div>
    <div class="member"><span class="avatar" style="background:#9a9a9a" role="img" aria-label="Member photo"></span><div><div class="name">ShamirDPatel</div><span class="follow"><svg viewBox="0 0 11 11"><circle cx="4" cy="3" r="2.3" fill="#4a90d9"/><path d="M0 11c0-3 2-4.5 4-4.5s4 1.5 4 4.5z" fill="#4a90d9"/></svg>Follow</span></div></div>
    <div class="member"><span class="avatar" style="background:#1f6b8a;border-radius:10px" role="img" aria-label="Member brand image"></span><div><div class="name">Autoresponder</div><span class="follow"><svg viewBox="0 0 11 11"><circle cx="4" cy="3" r="2.3" fill="#4a90d9"/><path d="M0 11c0-3 2-4.5 4-4.5s4 1.5 4 4.5z" fill="#4a90d9"/></svg>Follow</span></div></div>
    <div class="member"><span class="avatar" style="background:#b98366" role="img" aria-label="Member photo"></span><div><div class="name">kinseyfarrow</div><span class="follow"><svg viewBox="0 0 11 11"><circle cx="4" cy="3" r="2.3" fill="#4a90d9"/><path d="M0 11c0-3 2-4.5 4-4.5s4 1.5 4 4.5z" fill="#4a90d9"/></svg>Follow</span></div></div>
    <div class="member"><span class="avatar" style="background:#c48e6e" role="img" aria-label="Member photo"></span><div><div class="name">Carla_Amari_</div><span class="follow"><svg viewBox="0 0 11 11"><circle cx="4" cy="3" r="2.3" fill="#4a90d9"/><path d="M0 11c0-3 2-4.5 4-4.5s4 1.5 4 4.5z" fill="#4a90d9"/></svg>Follow</span></div></div>
    <div class="member"><span class="avatar" style="background:#a07a68" role="img" aria-label="Member photo"></span><div><div class="name">Carla_Amari_</div><span class="follow"><svg viewBox="0 0 11 11"><circle cx="4" cy="3" r="2.3" fill="#4a90d9"/><path d="M0 11c0-3 2-4.5 4-4.5s4 1.5 4 4.5z" fill="#4a90d9"/></svg>Follow</span></div></div>
    <div class="member"><span class="avatar" style="background:#eee;border-radius:4px" role="img" aria-label="Member brand image"></span><div><div class="name">smartbizpulse</div><span class="follow"><svg viewBox="0 0 11 11"><circle cx="4" cy="3" r="2.3" fill="#4a90d9"/><path d="M0 11c0-3 2-4.5 4-4.5s4 1.5 4 4.5z" fill="#4a90d9"/></svg>Follow</span></div></div>
  </div>

  <div class="feed-head"><h2>Retweet or Like To Earn More Credits</h2><span class="opt">Order by ⌄</span><span class="opt">Categories ⌄</span>
    <svg width="13" height="13" viewBox="0 0 15 15"><circle cx="6" cy="6" r="4.5" fill="none" stroke="#555" stroke-width="2"/><path d="M9.5 9.5l4 4" stroke="#555" stroke-width="2"/></svg></div>

  <article class="tweet"><span class="avatar" style="background:#8d6656" role="img" aria-label="Member photo"></span>
    <div class="meta"><span class="handle">@NoraDeane</span><span class="dot"></span>35 credits <span class="cat">[Affiliates]</span></div>
    <p>Lorem ipsum dolor sit amet, consectetuer adipiscing elit, sed diam <span class="link">http://www.lorumnibheuis.com</span><br>tincidunt utla coret dolore magna aliquam erat volutpat.<br><span class="link">#accumsan #lectores</span></p>
    <div class="actions"><span><svg width="11" height="11"><circle cx="5.5" cy="5.5" r="5.5" fill="#e0463c"/><path d="M3.5 3.5l4 4M7.5 3.5l-4 4" stroke="#fff" stroke-width="1.4"/></svg>Report Tweet</span><span><svg width="12" height="10"><path d="M0 5h9M6 1l4 4-4 4" stroke="#43a047" stroke-width="2" fill="none"/></svg>Skip</span><span><svg width="13" height="10"><path d="M2 2h8v4M11 8H3V4" stroke="#1b82d6" stroke-width="1.6" fill="none"/></svg>Schedule Retweet</span><span class="pill"><b class="like">Like</b><i>26</i></span><span class="pill"><b class="plus">+1</b><i>15</i></span></div>
  </article>

  <article class="tweet"><span class="avatar" style="background:#9a9a9a" role="img" aria-label="Member photo"></span>
    <div class="meta"><span class="handle">@SamirDPatel</span><span class="dot"></span>40 credits <span class="cat">[Personal Development]</span></div>
    <p>Duis autem vel eum iriure dolor in hendrerit in vulputate velit esse molestie consequat<br><span class="link">http://sho.rt/5Dt2A47</span><br><span class="link">#possim #etiam #processus</span></p>
    <div class="actions"><span><svg width="11" height="11"><circle cx="5.5" cy="5.5" r="5.5" fill="#e0463c"/><path d="M3.5 3.5l4 4M7.5 3.5l-4 4" stroke="#fff" stroke-width="1.4"/></svg>Report Tweet</span><span><svg width="12" height="10"><path d="M0 5h9M6 1l4 4-4 4" stroke="#43a047" stroke-width="2" fill="none"/></svg>Skip</span><span><svg width="13" height="10"><path d="M2 2h8v4M11 8H3V4" stroke="#1b82d6" stroke-width="1.6" fill="none"/></svg>Schedule Retweet</span><span class="pill"><b class="like">Like</b><i>26</i></span><span class="pill"><b class="plus">+1</b><i>15</i></span></div>
  </article>

  <article class="tweet hl"><span class="avatar" style="background:#2a2a2a;border-radius:10px" role="img" aria-label="Member brand image"></span>
    <div class="meta"><span class="handle">@GrowPlot</span><span class="dot"></span>51 credits <span class="cat">[Social Media]</span></div>
    <p>Claritas est etiam processus dynamicus, qui sequitur mutationem consuetudium lectorum. Mirum est notare<br>quam littera gothica, <span class="link">#quam</span> nunc putamus parum claram, <span class="link">#anteposuerit</span><br><span class="link">https://demonstraveris.com</span></p>
    <div class="actions"><span><svg width="11" height="11"><circle cx="5.5" cy="5.5" r="5.5" fill="#e0463c"/><path d="M3.5 3.5l4 4M7.5 3.5l-4 4" stroke="#fff" stroke-width="1.4"/></svg>Report Tweet</span><span><svg width="12" height="10"><path d="M0 5h9M6 1l4 4-4 4" stroke="#43a047" stroke-width="2" fill="none"/></svg>Skip</span><span><svg width="13" height="10"><path d="M2 2h8v4M11 8H3V4" stroke="#1b82d6" stroke-width="1.6" fill="none"/></svg>Schedule Retweet</span><span class="pill"><b class="like">Like</b><i>18</i></span><span class="pill"><b class="plus">+1</b><i>11</i></span></div>
  </article>

  <article class="tweet"><span class="avatar" style="background:#d9b98a" role="img" aria-label="Member photo"></span>
    <div class="meta"><span class="handle">@timefreelancer</span><span class="dot"></span>36 credits <span class="cat">[Business]</span></div>
    <p>Lorem ipsum dolor sit amet, consectetuer adipiscing elit, sed diam <span class="link">http://www.lorumnibheuis.com</span><br>tincidunt utla coret dolore magna aliquam erat volutpat.<br><span class="link">#accumsan #lectores</span></p>
    <div class="actions"><span><svg width="11" height="11"><circle cx="5.5" cy="5.5" r="5.5" fill="#e0463c"/><path d="M3.5 3.5l4 4M7.5 3.5l-4 4" stroke="#fff" stroke-width="1.4"/></svg>Report Tweet</span><span><svg width="12" height="10"><path d="M0 5h9M6 1l4 4-4 4" stroke="#43a047" stroke-width="2" fill="none"/></svg>Skip</span><span><svg width="13" height="10"><path d="M2 2h8v4M11 8H3V4" stroke="#1b82d6" stroke-width="1.6" fill="none"/></svg>Schedule Retweet</span><span class="pill"><b class="like">Like</b><i>26</i></span><span class="pill"><b class="plus">+1</b><i>15</i></span></div>
  </article>

  <article class="tweet"><span class="avatar" style="background:#8d6656" role="img" aria-label="Member photo"></span>
    <div class="meta"><span class="handle">@NoraDeane</span><span class="dot"></span>35 credits <span class="cat">[Affiliates]</span></div>
    <p>Lorem ipsum dolor sit amet, consectetuer adipiscing elit, sed diam <span class="link">http://www.lorumnibheuis.com</span><br>tincidunt utla coret dolore magna aliquam erat volutpat.<br><span class="link">#accumsan #lectores</span></p>
    <div class="actions"><span><svg width="11" height="11"><circle cx="5.5" cy="5.5" r="5.5" fill="#e0463c"/><path d="M3.5 3.5l4 4M7.5 3.5l-4 4" stroke="#fff" stroke-width="1.4"/></svg>Report Tweet</span><span><svg width="12" height="10"><path d="M0 5h9M6 1l4 4-4 4" stroke="#43a047" stroke-width="2" fill="none"/></svg>Skip</span><span><svg width="13" height="10"><path d="M2 2h8v4M11 8H3V4" stroke="#1b82d6" stroke-width="1.6" fill="none"/></svg>Schedule Retweet</span><span class="pill"><b class="like">Like</b><i>26</i></span><span class="pill"><b class="plus">+1</b><i>15</i></span></div>
  </article>

  <article class="tweet hl"><span class="avatar" style="background:radial-gradient(#f2c14e,#e86a5a 50%,#5aa0e0)" role="img" aria-label="Member brand image"></span>
    <div class="meta"><span class="handle">@crossnetideas</span><span class="dot"></span>5 credits <span class="cat">[Blog Platforms]</span></div>
    <p>Duis autem vel eum iriure dolor in hendrerit in vulputate velit esse molestie consequat, vel illum dolore eu<br>feugiat nulla facilisis <span class="link">http://www.crossnetidea.com/idea-15</span><br><span class="link">#accumsan #lectores</span></p>
    <div class="actions"><span><svg width="11" height="11"><circle cx="5.5" cy="5.5" r="5.5" fill="#e0463c"/><path d="M3.5 3.5l4 4M7.5 3.5l-4 4" stroke="#fff" stroke-width="1.4"/></svg>Report Tweet</span><span><svg width="12" height="10"><path d="M0 5h9M6 1l4 4-4 4" stroke="#43a047" stroke-width="2" fill="none"/></svg>Skip</span><span><svg width="13" height="10"><path d="M2 2h8v4M11 8H3V4" stroke="#1b82d6" stroke-width="1.6" fill="none"/></svg>Schedule Retweet</span><span class="pill"><b class="like">Like</b><i>26</i></span><span class="pill"><b class="plus">+1</b><i>15</i></span></div>
  </article>

  <article class="tweet"><span class="avatar" style="background:#7a5f52" role="img" aria-label="Member photo"></span>
    <div class="meta"><span class="handle">@markbrennan</span><span class="dot"></span>51 credits <span class="cat">[Business]</span></div>
    <p>Claritas est etiam processus dynamicus, qui sequitur mutationem consuetudium lectorum. Mirum est notare<br>quam littera gothica, <span class="link">#quam</span> nunc putamus parum claram, <span class="link">#anteposuerit</span><br><span class="link">https://demonstraveris.com</span></p>
    <div class="actions"><span><svg width="11" height="11"><circle cx="5.5" cy="5.5" r="5.5" fill="#e0463c"/><path d="M3.5 3.5l4 4M7.5 3.5l-4 4" stroke="#fff" stroke-width="1.4"/></svg>Report Tweet</span><span><svg width="12" height="10"><path d="M0 5h9M6 1l4 4-4 4" stroke="#43a047" stroke-width="2" fill="none"/></svg>Skip</span><span><svg width="13" height="10"><path d="M2 2h8v4M11 8H3V4" stroke="#1b82d6" stroke-width="1.6" fill="none"/></svg>Schedule Retweet</span><span class="pill"><b class="like">Like</b><i>2</i></span><span class="pill"><b class="plus">+1</b><i>2</i></span></div>
  </article>

  <article class="tweet"><span class="avatar" style="background:#b88a70" role="img" aria-label="Member photo"></span>
    <div class="meta"><span class="handle">@massestates</span><span class="dot"></span>36 credits <span class="cat">[Business]</span></div>
    <p>Duis autem vel eum iriure dolor in hendrerit in vulputate velit esse molestie consequat<br><span class="link">http://sho.rt/5Dt2A47</span><br><span class="link">#possim #etiam #processus</span></p>
    <div class="actions"><span><svg width="11" height="11"><circle cx="5.5" cy="5.5" r="5.5" fill="#e0463c"/><path d="M3.5 3.5l4 4M7.5 3.5l-4 4" stroke="#fff" stroke-width="1.4"/></svg>Report Tweet</span><span><svg width="12" height="10"><path d="M0 5h9M6 1l4 4-4 4" stroke="#43a047" stroke-width="2" fill="none"/></svg>Skip</span><span><svg width="13" height="10"><path d="M2 2h8v4M11 8H3V4" stroke="#1b82d6" stroke-width="1.6" fill="none"/></svg>Schedule Retweet</span><span class="pill"><b class="like">Like</b><i>0</i></span><span class="pill"><b class="plus">+1</b><i>78</i></span></div>
  </article>

  <svg class="spinner" width="40" height="40" viewBox="0 0 40 40">
    <g fill="#333"><circle cx="20" cy="4" r="3"/><circle cx="31.3" cy="8.7" r="2.8" opacity=".9"/><circle cx="36" cy="20" r="2.6" opacity=".8"/><circle cx="31.3" cy="31.3" r="2.4" opacity=".7"/><circle cx="20" cy="36" r="2.2" opacity=".6"/><circle cx="8.7" cy="31.3" r="2" opacity=".5"/><circle cx="4" cy="20" r="1.8" opacity=".4"/><circle cx="8.7" cy="8.7" r="1.6" opacity=".3"/></g>
  </svg>
</main>

<aside class="side">
  <div class="credits">
    <div class="label">Your Credits</div>
    <div class="num">315858</div>
    <div class="btn"><svg width="22" height="18" viewBox="0 0 22 18"><path d="M2 9l8-7v4c6 0 10 3 10 10-2-4-5-5-10-5v4z" fill="#fff"/></svg>Submit a Retweet</div>
  </div>

  <section class="engage">
    <div class="section-head"><h2>Engage</h2><span class="sub">Members who shared your tweets</span></div>
    <div class="list">
      <div class="member"><span class="avatar" style="background:#6b4a3a" role="img" aria-label="Member photo"></span><div><div class="name">devansh</div><span class="follow"><svg viewBox="0 0 11 11"><circle cx="4" cy="3" r="2.3" fill="#4a90d9"/><path d="M0 11c0-3 2-4.5 4-4.5s4 1.5 4 4.5z" fill="#4a90d9"/></svg>Follow</span></div></div>
      <div class="member"><span class="avatar" style="background:#a27560" role="img" aria-label="Member photo"></span><div><div class="name">Franchise</div><span class="follow"><svg viewBox="0 0 11 11"><circle cx="4" cy="3" r="2.3" fill="#4a90d9"/><path d="M0 11c0-3 2-4.5 4-4.5s4 1.5 4 4.5z" fill="#4a90d9"/></svg>Follow</span></div></div>
      <div class="member"><span class="avatar" style="background:#e2552f" role="img" aria-label="Member brand image"></span><div><div class="name">ProBlogWins</div><span class="follow"><svg viewBox="0 0 11 11"><circle cx="4" cy="3" r="2.3" fill="#4a90d9"/><path d="M0 11c0-3 2-4.5 4-4.5s4 1.5 4 4.5z" fill="#4a90d9"/></svg>Follow</span></div></div>
      <div class="member"><span class="avatar" style="background:#8a6a3a" role="img" aria-label="Member photo"></span><div><div class="name">ManuelMarin</div><span class="follow"><svg viewBox="0 0 11 11"><circle cx="4" cy="3" r="2.3" fill="#4a90d9"/><path d="M0 11c0-3 2-4.5 4-4.5s4 1.5 4 4.5z" fill="#4a90d9"/></svg>Follow</span></div></div>
      <div class="member"><span class="avatar" style="background:#c98e5a" role="img" aria-label="Member illustrated avatar"></span><div><div class="name">moumitaj</div><span class="follow"><svg viewBox="0 0 11 11"><circle cx="4" cy="3" r="2.3" fill="#4a90d9"/><path d="M0 11c0-3 2-4.5 4-4.5s4 1.5 4 4.5z" fill="#4a90d9"/></svg>Follow</span></div></div>
      <div class="member"><span class="avatar" style="background:#7a5f52" role="img" aria-label="Member photo"></span><div><div class="name">markbrennan</div><span class="follow"><svg viewBox="0 0 11 11"><circle cx="4" cy="3" r="2.3" fill="#4a90d9"/><path d="M0 11c0-3 2-4.5 4-4.5s4 1.5 4 4.5z" fill="#4a90d9"/></svg>Follow</span></div></div>
    </div>
  </section>

  <section style="margin-top:60px">
    <div class="section-head"><h2>Featured Websites</h2><span class="sub">See all websites</span></div>
    <div class="slide" role="img" aria-label="Screenshot of featured website header">
      <span class="arrow l"><svg width="8" height="12"><path d="M7 1L2 6l5 5" stroke="#333" stroke-width="2" fill="none"/></svg></span>
      <span class="arrow r"><svg width="8" height="12"><path d="M1 1l5 5-5 5" stroke="#333" stroke-width="2" fill="none"/></svg></span>
    </div>
    <div class="card-title">SEO Tips And Blogging Tips For<br>Bloggers And Website Owners</div>
    <div class="card-text">Helping everyday website owners &amp; bloggers through engaging topics about traffic, link building, monetization and more...</div>
    <div class="dots"><i></i><i></i></div>
  </section>

  <section style="margin-top:60px">
    <div class="section-head"><h2>Our Blog</h2><span class="sub">See all blogs</span></div>
    <div class="blog-img" role="img" aria-label="Blog post illustration: speech bubble with a heart on a blue sunburst">
      <span class="arrow l"><svg width="8" height="12"><path d="M7 1L2 6l5 5" stroke="#333" stroke-width="2" fill="none"/></svg></span>
      <span class="arrow r"><svg width="8" height="12"><path d="M1 1l5 5-5 5" stroke="#333" stroke-width="2" fill="none"/></svg></span>
    </div>
    <div class="card-title">How to Use FaceSpace Contests<br>to Explode Your Traffic</div>
    <div class="card-text">Social media isn't going anywhere. Even with more people using their mobile devices...</div>
    <div class="dots"><i></i><i></i></div>
  </section>
</aside>

<section class="contest">See who won our PostLoopy Labor Day Contest <span class="btn">Click Here</span></section>

<footer class="footer">
  <div class="logo">PostLoopy</div>
  <nav><a>Home</a><a>About Us</a><a>How It Works</a><a>Refund Policy</a><a>Contact Us</a><a>Privacy Policy</a><a>Terms &amp; Conditions</a></nav>
</footer>

<div class="bottom">
  <div class="social"><i></i><i></i><i></i><i></i><i></i></div>
  <span class="totop"><svg width="14" height="9"><path d="M1 8l6-6 6 6" stroke="#cfe3f6" stroke-width="1.6" fill="none"/></svg></span>
  <div>Copyright © 2014 <b>PostLoopy</b> All rights reserved.</div>
</div>

</body>
</html>
```